Dental Stationary
business card
Creative Brief
Modern
Peter Holbrook DDS, Marian Covelli, DDS
4153 County Rd #6 PO Box 562 Millbrook Falls, NY 12057
info@brightmeadowdentalcare.com
www.brightmeadowdentalcare.com
have not received logo source files yet
We welcome new patients. All consultations are complimentary

```html
<!DOCTYPE html>
<html lang="en">
<head>
<meta charset="utf-8">
<title>Bright Meadow Dental Care – Business Card</title>
<link href="https://fonts.googleapis.com/css2?family=Cinzel:wght@400&family=EB+Garamond:wght@400&display=swap" rel="stylesheet">
<style>
  :root {
    --backdrop: #d9dadc;
    --navy: #172a4f;
    --paper: #ffffff;
    --taupe: #9b8a78;
    --ink: #1f2f52;
  }
  * { margin: 0; padding: 0; box-sizing: border-box; }
  html, body { width: 1200px; height: 908px; overflow: hidden; }
  body {
    background: var(--backdrop);
    display: flex;
    flex-direction: column;
    align-items: center;
    justify-content: center;
    gap: 36px;
  }
  .card {
    width: 700px;
    height: 400px;
    position: relative;
    box-shadow: 0 6px 18px rgba(0,0,0,0.18);
  }
  .card-front {
    background: var(--navy);
    display: flex;
    align-items: center;
    justify-content: center;
  }
  .card-back { background: var(--paper); }

  .brand-name {
    font-family: "Cinzel", serif;
    font-weight: 400;
    text-align: center;
    line-height: 1.15;
    letter-spacing: 0.04em;
  }
  .card-front .brand-name { color: var(--paper); font-size: 40px; }
  .card-back .brand-name {
    position: absolute;
    left: 64px;
    top: 72px;
    color: var(--ink);
    font-size: 30px;
    text-align: left;
  }

  .contact {
    position: absolute;
    left: 64px;
    top: 200px;
    font-family: "EB Garamond", serif;
    font-style: normal;
    color: var(--ink);
    font-size: 16px;
    line-height: 1.45;
  }
  .contact-line { display: flex; align-items: center; gap: 8px; }
  .contact-icon {
    width: 15px; height: 15px;
    flex: none;
  }

  .dentists {
    position: absolute;
    right: 56px;
    top: 92px;
    text-align: right;
    font-family: "Cinzel", serif;
    color: var(--ink);
    font-size: 17px;
    line-height: 1.5;
    letter-spacing: 0.03em;
  }
</style>
</head>
<body>

  <section class="card card-front">
    <p class="brand-name">Bright Meadow<br>Dental Care</p>
  </section>

  <section class="card card-back">
    <p class="brand-name">Bright Meadow<br>Dental Care</p>

    <address class="contact">
      <div>4153 County Rd #6</div>
      <div>PO Box 562</div>
      <div>Millbrook Falls, NY 12057</div>
      <div class="contact-line">
        <svg class="contact-icon" viewBox="0 0 16 16" aria-hidden="true">
          <circle cx="8" cy="8" r="8" fill="#9b8a78"/>
          <path d="M5 4.2l1.6-.3.9 2-1 .8a5 5 0 0 0 2.8 2.8l.8-1 2 .9-.3 1.6c-4 .5-7.3-2.8-6.8-6.8z" fill="#fff"/>
        </svg>
        <span>518-555-0142</span>
      </div>
      <div class="contact-line">
        <svg class="contact-icon" viewBox="0 0 16 16" aria-hidden="true">
          <circle cx="8" cy="8" r="8" fill="#9b8a78"/>
          <path d="M5.6 4.5h4.8a.6.6 0 0 1 .6.6v5.8a.6.6 0 0 1-.6.6H5.6a.6.6 0 0 1-.6-.6V5.1a.6.6 0 0 1 .6-.6z" fill="#fff"/>
        </svg>
        <span>518-555-0187</span>
      </div>
      <div class="contact-line">
        <svg class="contact-icon" viewBox="0 0 16 16" aria-hidden="true">
          <circle cx="8" cy="8" r="8" fill="#9b8a78"/>
          <rect x="4" y="5" width="8" height="6" fill="none" stroke="#fff" stroke-width="1"/>
          <path d="M4 5l4 3.2L12 5" fill="none" stroke="#fff" stroke-width="1"/>
        </svg>
        <span>info@brightmeadowdentalcare.com</span>
      </div>
      <div class="contact-line">
        <svg class="contact-icon" viewBox="0 0 16 16" aria-hidden="true">
          <circle cx="8" cy="8" r="8" fill="#9b8a78"/>
          <circle cx="8" cy="8" r="4" fill="none" stroke="#fff" stroke-width="1"/>
          <path d="M4 8h8M8 4c-1.6 2.4-1.6 5.6 0 8M8 4c1.6 2.4 1.6 5.6 0 8" fill="none" stroke="#fff" stroke-width="0.9"/>
        </svg>
        <span>www.brightmeadowdentalcare.com</span>
      </div>
    </address>

    <div class="dentists">
      <p>Peter Holbrook DDS</p>
      <p>Marian Covelli, DDS</p>
    </div>
  </section>

</body>
</html>
```